Mirabo & Orvan Automotive Repair Shop. Need a new website design.

We specialize in Mirabo & Orvan auto repair, but also work on other Asian import vehicles. We have been in business for 7 years and pride ourselves on high quality auto repair that is fixed right the first time. Would like the automotive repair website to incorporate the colors black, red and white if possible and have our logo and some Mirabo and Orvan vehicles included in the website.

Target Market(s)

Mirabo & Orvan vehicle owners

Industry/Entity Type

Automotive Repair

Coding

Coded - Design and coding required

Number of Pages Required

5+ page

Colors
EB3D1F
EC4F4E
F09395
F8D3D4
FCEDEE

Requirements
Must have
• Home, Services, Contact Us, Schedule appointment, and a gallery tab that I can add shop pictures to when completed.
Nice to have
• Would like to see example pictures of job next to each service listed.
Should not have
• Service not related to auto repair. Ex. auto detailing, towing, car wash

```html
<!DOCTYPE html>
<html lang="en">
<head>
<meta charset="utf-8">
<title>Corvid Automotive – Mirabo &amp; Orvan Auto Repair</title>
<link href="https://fonts.googleapis.com/css2?family=Michroma&family=Barlow:wght@400;500;600;700&display=swap" rel="stylesheet">
<style>
:root{
  --red:#e3120b;
  --red-dark:#b80d08;
  --black:#0d0d0d;
  --dark:#161616;
  --grey:#8a8a8a;
  --line:#d9d9d9;
  --white:#ffffff;
  --silver-1:#f2f2f2;
  --silver-2:#c9c9c9;
  --head:"Michroma",sans-serif;
  --body:"Barlow",sans-serif;
}
*{margin:0;padding:0;box-sizing:border-box}
html,body{width:1200px;height:4612px;overflow:hidden}
body{position:relative;background:var(--white);font-family:var(--body);color:var(--black)}
.abs{position:absolute}
.btn{position:absolute;display:flex;align-items:center;justify-content:center;background:var(--red);color:var(--white);font-family:var(--body);font-weight:700;font-size:15px;letter-spacing:.3px;text-transform:uppercase}
.btn--outline{background:transparent;border:2px solid var(--red);color:var(--red);letter-spacing:2px;font-size:14px}
.eyebrow{font-family:var(--head);color:var(--red);font-size:15px;letter-spacing:1px}
.title{font-family:var(--head);font-size:32px;letter-spacing:2px}
.photo{position:absolute}

/* header & hero */
.hero{position:absolute;left:0;top:0;width:1200px;height:790px;background:radial-gradient(ellipse at 70% 40%,#2a2a2a 0%,#141414 55%,#0a0a0a 100%)}
.nav a{position:absolute;top:72px;color:var(--white);font-size:14px;text-decoration:none;font-weight:500}
.nav a.active{border-bottom:2px solid var(--red);padding-bottom:6px}
.nav-btn{position:absolute;left:917px;top:58px;width:199px;height:36px;border:1.5px solid var(--white);color:var(--white);font-size:12px;font-weight:600;display:flex;align-items:center;justify-content:center}
.brand{position:absolute;display:flex;align-items:center;gap:10px;color:var(--white);font-family:var(--head);font-size:20px;letter-spacing:1px}
.brand-dot{width:16px;height:16px;border-radius:50%;background:var(--red)}
.hero-frame{position:absolute;left:125px;top:247px;width:50px;height:366px;border:3px solid var(--white);border-right:none}
.hero-h{position:absolute;left:168px;top:290px;font-family:var(--head);font-size:34px;line-height:42px;color:var(--white);letter-spacing:1px}
.hero-h .red{color:var(--red);font-size:29px}
.hero-p{position:absolute;left:172px;top:418px;width:390px;color:#e4e4e4;font-size:16px;line-height:26px}
.engine{position:absolute;left:595px;top:235px;width:480px;height:390px;border-radius:30px;background:radial-gradient(circle,#6d6d6d 0%,#3a3a3a 45%,rgba(20,20,20,0) 75%)}
.scroll{position:absolute;left:594px;top:607px;width:18px;height:30px;border:2px solid var(--white);border-radius:9px}

/* about */
.about-photo{left:112px;top:853px;width:346px;height:402px;background:linear-gradient(160deg,#5a5a55,#2b2b2b 60%,#454545)}
.years{position:absolute;left:458px;top:1165px;width:127px;height:113px;background:var(--red);color:var(--white);text-align:center;padding-top:14px}
.years b{font-family:var(--head);font-size:34px;display:block;line-height:40px}
.years span{font-size:14px;font-weight:600;line-height:17px;display:block}
.about-text{position:absolute;left:612px;top:935px;width:520px}
.about-text .lead{font-size:16px;font-weight:600;line-height:23px}
.about-text .copy{margin-top:18px;font-size:14.3px;line-height:23px;color:#333}

/* partners */
.partners{position:absolute;left:110px;top:1360px;width:960px;height:255px;background:var(--white);box-shadow:0 4px 18px rgba(0,0,0,.15);z-index:2}
.partners h3{font-family:var(--head);font-size:17px;text-align:center;margin-top:32px;line-height:25px;letter-spacing:1px}
.badge{position:absolute;top:120px;height:100px;background:#e8e8e8}

/* services */
.services{position:absolute;left:0;top:1540px;width:1200px;height:700px;background:radial-gradient(ellipse at 50% 20%,#2b2b2b,#0c0c0c 70%)}
.svc{position:absolute;display:flex;align-items:flex-start;gap:12px;color:var(--white);font-size:15.5px;line-height:22px}
.svc svg{flex:none;margin-top:-2px}
.svc-active{position:absolute;left:97px;top:1788px;width:285px;height:50px;background:var(--red);clip-path:polygon(0 0,100% 0,94% 100%,0 100%)}

/* gallery */
.gallery{position:absolute;left:0;top:2230px;width:1200px;height:860px;background:linear-gradient(100deg,#e9e9e9 0%,#bdbdbd 35%,#f4f4f4 55%,#b7b7b7 80%,#dcdcdc 100%)}

/* makes */
.makes-h{position:absolute;left:0;top:3158px;width:1200px;text-align:center;font-family:var(--head);font-size:19px;line-height:25px;letter-spacing:1px}
.makes{position:absolute;left:130px;top:3282px;width:920px;height:286px;display:grid;grid-template-columns:repeat(4,1fr);grid-template-rows:repeat(2,1fr);border:1px solid var(--line)}
.make{border:1px solid var(--line);display:flex;flex-direction:column;align-items:center;justify-content:center;gap:10px;font-family:var(--body);font-weight:700;font-size:22px;letter-spacing:2px;color:#2a2a2a}
.make i{width:36px;height:36px;border:3px solid #2a2a2a;border-radius:50%}
.make.silver{background:linear-gradient(100deg,#dcdcdc,#a9a9a9 50%,#e6e6e6)}
.make.silver i{border-color:var(--red)}

/* contact */
.contact{position:absolute;left:0;top:3750px;width:1200px;height:640px;background:linear-gradient(90deg,#121212 0%,#2c2c2c 45%,#3a3a3a 100%)}
.form{position:absolute;left:595px;top:3842px;width:490px;height:390px;border:2px solid #7a7a7a;border-radius:12px;background:rgba(0,0,0,.55)}
.form h4{position:absolute;left:40px;top:34px;font-family:var(--head);color:var(--white);font-size:16px;letter-spacing:1px}
.field{position:absolute;border:1px solid #cfcfcf;color:var(--white);font-size:11px;padding:9px 0 0 12px}

/* footer */
.footer-nav a{position:absolute;top:4450px;font-weight:700;font-size:17px;color:var(--black);text-decoration:none}
.footer-nav i{position:absolute;top:4459px;width:6px;height:6px;background:var(--red)}
.social{position:absolute;top:4540px;display:flex;align-items:center;gap:5px;font-size:13px;font-weight:600}
.social i{width:16px;height:16px;border-radius:50%;background:var(--red)}
</style>
</head>
<body>

<!-- header + hero -->
<section class="hero">
  <nav class="nav">
    <a class="active" style="left:162px">HOME</a>
    <a style="left:246px">ABOUT US</a>
    <a style="left:356px">OUR SERVICES</a>
    <a style="left:722px">GALLERY</a>
    <a style="left:830px">CONTACT</a>
  </nav>
  <div class="nav-btn">SCHEDULE AN APPOINTMENT</div>
  <div class="brand" style="left:505px;top:68px"><span class="brand-dot"></span>CORVID</div>

  <div class="hero-frame"></div>
  <h1 class="hero-h">LOCALLY OWNED<br>AUTO REPAIR<br><span class="red">SHOP IN BROOKDALE</span></h1>
  <p class="hero-p">Corvid Automotive is a locally owned and operated auto repair shop in Brookdale that offers comprehensive car care and services</p>
  <div class="btn" style="left:172px;top:505px;width:282px;height:55px">SCHEDULE AN APPOINTMENT</div>
  <div class="engine" role="img" aria-label="X-ray style illustration of a V engine block"></div>
  <div class="scroll"></div>
</section>
<svg class="abs" style="left:0;top:660px" width="1200" height="140" viewBox="0 660 1200 140">
  <polygon points="0,680 600,735 1200,690 1200,800 0,800" fill="#ffffff"/>
  <polygon points="0,680 600,735 1200,690 1200,795 600,748 0,790" fill="var(--red)"/>
</svg>

<!-- about -->
<div class="abs" style="left:104px;top:840px;width:60px;height:46px;background:var(--red)"></div>
<div class="abs" style="left:104px;top:1170px;width:50px;height:92px;background:#2a2a2a"></div>
<div class="photo about-photo" role="img" aria-label="Technician working under a lifted vehicle in the shop"></div>
<div class="years"><b>20</b><span>YEARS OF<br>EXPERIENCE</span></div>
<div class="eyebrow abs" style="left:610px;top:852px">OUR COMPANY</div>
<h2 class="title abs" style="left:610px;top:876px">ABOUT CORVID</h2>
<div class="abs" style="left:968px;top:890px;width:8px;height:8px;background:var(--red)"></div>
<div class="abs" style="left:985px;top:893px;width:215px;height:2px;background:var(--red)"></div>
<div class="about-text">
  <p class="lead">Corvid Automotive is a locally owned and operated auto repair shop in Brookdale that offers comprehensive car care and services for Mirabo &amp; Orvan and all other Asian imports vehicles.</p>
  <p class="copy">Led by an NCT master certified technician with 20 years experience working for Mirabo &amp; Orvan dealerships, our auto shop is your go to facility for everything from factory auto maintenance, including oil changes, fluid services and tune ups, to complex engine repairs, hybrid diagnostic &amp; repair, brake jobs, etc. We have state of the art equipment and tools to ensure that we can properly diagnose and repair your vehicle to get you back on the road quickly. Our work comes with a warranty and we offer towing if needed. We also offer discounts for Ridely &amp; Hoppa rides.</p>
</div>
<div class="btn btn--outline" style="left:617px;top:1225px;width:167px;height:47px">LEARN MORE</div>

<!-- services background -->
<section class="services"></section>

<!-- partners -->
<div class="abs" style="left:104px;top:1354px;width:70px;height:50px;background:var(--red);z-index:1"></div>
<div class="abs" style="left:1010px;top:1555px;width:66px;height:66px;background:var(--red);z-index:1"></div>
<div class="partners">
  <h3>AUTHORIZED INSTALLER FOR DURAFLOW OIL,<br>KEYSTONE CELLS</h3>
  <div class="badge" style="left:122px;width:84px;border-radius:6px" role="img" aria-label="Technician certification badge"></div>
  <div class="badge" style="left:300px;width:100px;border-radius:50%" role="img" aria-label="Best of Brookdale award badge"></div>
  <div class="badge" style="left:500px;width:140px;height:80px;top:130px" role="img" aria-label="Keystone Cells partner badge"></div>
  <div class="badge" style="left:710px;width:170px;height:44px;top:148px" role="img" aria-label="Duraflow partner badge"></div>
</div>

<div class="eyebrow abs" style="left:0;width:1200px;text-align:center;top:1687px">WHAT WE DO</div>
<h2 class="title abs" style="left:0;width:1200px;text-align:center;top:1707px;color:var(--white)">SERVICES PROVIDE</h2>

<div class="svc-active"></div>
<svg width="0" height="0" style="position:absolute">
  <symbol id="ico" viewBox="0 0 28 28"><rect x="3" y="3" width="22" height="22" rx="5" fill="none" stroke="#fff" stroke-width="2"/><circle cx="14" cy="14" r="4" fill="none" stroke="#fff" stroke-width="2"/></symbol>
</svg>

<div class="svc" style="left:120px;top:1805px"><svg width="28" height="28"><use href="#ico"/></svg>Oil Changes</div>
<div class="svc" style="left:120px;top:1851px"><svg width="28" height="28"><use href="#ico"/></svg>Computer Diagnostics</div>
<div class="svc" style="left:120px;top:1897px"><svg width="28" height="28"><use href="#ico"/></svg>Electrical Specialists</div>
<div class="svc" style="left:120px;top:1943px"><svg width="28" height="28"><use href="#ico"/></svg>Tires</div>
<div class="svc" style="left:120px;top:1989px"><svg width="28" height="28"><use href="#ico"/></svg>Tire Balance &amp; Rotations</div>
<div class="svc" style="left:120px;top:2035px"><svg width="28" height="28"><use href="#ico"/></svg>Pre Purchase Inspections</div>
<div class="svc" style="left:120px;top:2081px"><svg width="28" height="28"><use href="#ico"/></svg>Insurance Claims</div>
<div class="svc" style="left:120px;top:2127px"><svg width="28" height="28"><use href="#ico"/></svg>Emission Repair &amp; Catalytic<br>Converters</div>

<div class="svc" style="left:428px;top:1805px"><svg width="28" height="28"><use href="#ico"/></svg>Engine Repair</div>
<div class="svc" style="left:428px;top:1851px"><svg width="28" height="28"><use href="#ico"/></svg>Heating &amp; AC Repair</div>
<div class="svc" style="left:428px;top:1897px"><svg width="28" height="28"><use href="#ico"/></svg>State Inspection</div>
<div class="svc" style="left:428px;top:1943px"><svg width="28" height="28"><use href="#ico"/></svg>Suspension Service &amp; Repair</div>
<div class="svc" style="left:428px;top:1989px"><svg width="28" height="28"><use href="#ico"/></svg>Leveling Kits &amp; Minor Lift Kit installation</div>
<div class="svc" style="left:428px;top:2035px"><svg width="28" height="28"><use href="#ico"/></svg>Brakes Service &amp; Repair</div>
<div class="svc" style="left:428px;top:2081px"><svg width="28" height="28"><use href="#ico"/></svg>Exhaust, Muffler Service &amp; Repair</div>
<div class="svc" style="left:428px;top:2127px"><svg width="28" height="28"><use href="#ico"/></svg>Automatic, Manual, Computerized<br>Transmission Service &amp; Repair</div>

<div class="svc" style="left:790px;top:1805px"><svg width="28" height="28"><use href="#ico"/></svg>Clutch Service &amp; Repair</div>
<div class="svc" style="left:790px;top:1851px"><svg width="28" height="28"><use href="#ico"/></svg>CV Axle Service &amp; Repair</div>
<div class="svc" style="left:790px;top:1897px"><svg width="28" height="28"><use href="#ico"/></svg>Fuel Injection System Service<br>Cleaning &amp; Repair</div>
<div class="svc" style="left:790px;top:1966px"><svg width="28" height="28"><use href="#ico"/></svg>Timing Belts &amp; Water Pumps</div>
<div class="svc" style="left:790px;top:2012px"><svg width="28" height="28"><use href="#ico"/></svg>Radiators &amp; Fans Service &amp; Repair</div>
<div class="svc" style="left:790px;top:2058px"><svg width="28" height="28"><use href="#ico"/></svg>Tune ups &amp; Factory Scheduled<br>Maintenance</div>
<div class="svc" style="left:790px;top:2127px"><svg width="28" height="28"><use href="#ico"/></svg>Hybrid Vehicle diagnostic &amp; repair<br>24-hr Night Drop</div>

<!-- gallery -->
<section class="gallery"></section>
<svg class="abs" style="left:0;top:2200px" width="1200" height="110" viewBox="0 2200 1200 110">
  <polygon points="0,2200 1200,2200 1200,2215 600,2280 0,2215" fill="#0e0e0e"/>
  <polygon points="0,2215 600,2280 1200,2215 1200,2255 600,2300 0,2262" fill="var(--red)"/>
</svg>
<div class="eyebrow abs" style="left:0;width:1200px;text-align:center;top:2416px">PHOTO GALLERY</div>
<h2 class="title abs" style="left:0;width:1200px;text-align:center;top:2438px">OUR GALLERY</h2>
<div class="photo" style="left:107px;top:2512px;width:323px;height:238px;background:linear-gradient(150deg,#6a6a66,#2d2d2d)" role="img" aria-label="Mechanic working on a wheel hub"></div>
<div class="photo" style="left:442px;top:2512px;width:323px;height:238px;background:linear-gradient(150deg,#8b8b8b,#2a2a2a 60%,#7b3030)" role="img" aria-label="Open engine bay of an Orvan SUV"></div>
<div class="photo" style="left:777px;top:2512px;width:323px;height:238px;background:linear-gradient(150deg,#4b5660,#242a30)" role="img" aria-label="Engine disassembled for rebuild"></div>
<div class="photo" style="left:110px;top:2770px;width:488px;height:235px;background:linear-gradient(150deg,#3e5a8a,#8a8d92 50%,#4a4a4a)" role="img" aria-label="Silver Mirabo pickup on a lift"></div>
<div class="photo" style="left:612px;top:2770px;width:488px;height:235px;background:linear-gradient(180deg,#c9c2b6,#8d8a85 55%,#4f4f4f)" role="img" aria-label="Row of Mirabo SUVs parked outside the shop"></div>

<!-- makes -->
<h2 class="makes-h">CORVID AUTOMOTIVE SPECIALIZES IN MIRABO &amp; ORVAN<br>AUTO REPAIR BUT ALSO SERVICE AND REPAIR<br>THE FOLLOWING MAKES</h2>
<div class="makes">
  <div class="make"><i></i>ARVEX</div>
  <div class="make"><i></i>HANVO</div>
  <div class="make"><i></i>INORA</div>
  <div class="make"><i></i>KAYDO</div>
  <div class="make silver"><i></i>MIRASHI</div>
  <div class="make"><i></i>MAZORA</div>
  <div class="make"><i></i>NISARO</div>
  <div class="make"><i></i>HONDREL</div>
</div>
<div class="btn" style="left:445px;top:3607px;width:292px;height:56px">SCHEDULE AN APPOINTMENT</div>

<!-- contact -->
<section class="contact" role="img" aria-label="Dark shop background with a car front and engine parts"></section>
<div class="abs" style="left:0;top:3932px;width:112px;height:2px;background:var(--red)"></div>
<div class="eyebrow abs" style="left:135px;top:3897px">GET IN TOUCH</div>
<h2 class="title abs" style="left:135px;top:3922px;color:var(--white)">CONTACT <span style="color:var(--red)">US</span></h2>
<p class="abs" style="left:135px;top:3982px;width:390px;color:#e6e6e6;font-size:15.5px;line-height:27px">Contact us for a free estimate! Please include year, make, and model and the service or repair you would like repair you would like an estimate on.</p>
<div class="btn" style="left:138px;top:4088px;width:237px;height:44px;font-size:13px">SCHEDULE AN APPOINTMENT</div>
<div class="form">
  <h4>LEAVE US A MESSAGE</h4>
</div>
<div class="field" style="left:635px;top:3912px;width:203px;height:38px">First Name*</div>
<div class="field" style="left:845px;top:3912px;width:203px;height:38px">Last Name*</div>
<div class="field" style="left:635px;top:3963px;width:203px;height:38px">Email address*</div>
<div class="field" style="left:845px;top:3963px;width:203px;height:38px">Phone*</div>
<div class="field" style="left:635px;top:4013px;width:413px;height:80px">Message</div>
<div class="btn" style="left:638px;top:4128px;width:130px;height:37px;font-family:var(--head);font-size:12px">SUBMIT</div>

<!-- footer -->
<svg class="abs" style="left:0;top:4260px" width="1200" height="352" viewBox="0 4260 1200 352">
  <polygon points="0,4330 600,4278 1200,4330 1200,4612 0,4612" fill="#ffffff"/>
  <polygon points="0,4330 600,4278 1200,4330 1200,4372 600,4318 0,4372" fill="var(--red)"/>
</svg>
<div class="abs" style="left:520px;top:4330px;width:160px;height:86px;background:var(--black);display:flex;align-items:center;justify-content:center"><div class="brand" style="position:static;font-size:18px"><span class="brand-dot"></span>CORVID</div></div>
<nav class="footer-nav">
  <a style="left:248px">HOME</a><i style="left:328px"></i>
  <a style="left:373px">ABOUT US</a><i style="left:487px"></i>
  <a style="left:531px">OUR SERVICES</a><i style="left:681px"></i>
  <a style="left:725px">GALLERY</a><i style="left:837px"></i>
  <a style="left:877px">CONTACT</a>
</nav>
<p class="abs" style="left:0;width:1200px;text-align:center;top:4500px;font-size:13px;color:#333">Copyright © 2024 Corvid Automotive. All rights reserved.</p>
<div class="social" style="left:468px"><i></i>Friendly</div>
<div class="social" style="left:552px"><i></i>Chirp</div>
<div class="social" style="left:614px"><i></i>Linkwork</div>
<div class="social" style="left:694px"><i></i>Snapgram</div>

</body>
</html>
```